We are a printed circuit board manufacturer. Need a company professional web site to allow our potential customers to know more about our background, capability and our products. The web site will contain three languages, which are Chinese, English and Japanese. Our audience are mainly electronic companies that procure printed circuit boards. I have a word document that have all the required text in all three languages. The final design should communicate the impression that we embrace quality, trustworthiness and long term partnership business principles.
We should have sections that allow us to post pictures of our facilities.
I have added the three files in three different languages.
Some of the information is below:
Background
RVD Worldwide Limited (RVD) was set up in Hong Kong in 2007 by two Hong Kong entrepreneurs, Mr. Lok Fai Tam and Mr. Wai Ho. We acquired the single sided printed circuit board factory located in Dongguan City, Guangdong Province, China, from Valtor Corporation of the U.S. in 2007. In addition to RVD, Mr. Tam and Mr. Ho also own Brightrail Systems Company Limited, a semiconductor company based in Hong Kong since 1997 with a total investment of over US$100 million. Brightrail is engaged in the manufacturing of flexible substrates and MEMS assembly business.
RVD has been awarded TS 16949 and ISO14000 certificates since 2009 and 2004 respectively.
Business Principles
RVD Worldwide Limited strives to be a professional top notched printed circuit board supplier. We embrace four “EXCELLENCE” principles, namely, excellence in quality, excellence in prices, excellence in services and excellence in on time delivery.
We approach each customer with a long-term partnership view that delivers the lowest ownership costs and highest total values to our customers. We customize quotations and solutions in order to allow our customers to win more businesses. We believe by thinking from our customers’ points of view we will be able to create a WIN-WIN relationship.
Customers
Due to our excellent quality, services and production systems, RVD Worldwide Limited manage to service a number of large Japanese and US customers, which include:
Technical capability overview
Below is an overview of our current capability:
Target Market(s)
Electronic companies buyers
Industry/Entity Type
Business
Requirements
Must have
- Capability description
Should not have
- no cartoon

```html
<!DOCTYPE html>
<html lang="en">
<head>
<meta charset="utf-8">
<title>RVD Worldwide Limited</title>
<link rel="stylesheet" href="https://fonts.googleapis.com/css2?family=Open+Sans:wght@400;600;700&family=Arimo:wght@400&display=swap">
<style>
:root{
  --white:#ffffff;
  --page:#f0f0f0;
  --band:#d9d9d9;
  --rule:#555555;
  --footer:#333333;
  --ink:#2b2b2b;
  --ink-soft:#3a3a3a;
  --green:#128a6b;
  --green-dot:#16c26a;
  --grey-btn:#a3a3a3;
  --brand:#1f8a5c;
}
*{margin:0;padding:0;box-sizing:border-box}
html,body{width:1200px;height:1114px;overflow:hidden;background:var(--white)}
body{position:relative;font-family:"Open Sans",sans-serif;color:var(--ink)}
.abs{position:absolute}

.site-header{left:0;top:0;width:1200px;height:190px;background:var(--white)}
.brand{left:118px;top:56px;width:240px;font-family:"Open Sans",sans-serif;font-weight:700;color:var(--brand);font-size:30px;line-height:34px;text-align:center}
.languages{left:930px;top:50px;display:flex;gap:10px}
.languages svg{display:block}
.phone{left:931px;top:93px;font-family:"Arimo",sans-serif;font-size:17px;color:var(--ink-soft)}
.main-nav{left:0;top:166px;width:1200px;height:24px}
.main-nav a{position:absolute;font-size:16px;color:var(--ink-soft);text-decoration:none}
.header-rule{left:0;top:190px;width:1200px;height:12px;background:var(--rule)}

.content{left:0;top:202px;width:1200px;height:713px;background:var(--page)}
.facility-photo{left:139px;top:243px;width:408px;height:306px;background:linear-gradient(160deg,#c9cdc8 0%,#a9b0aa 45%,#7d847f 100%)}
.slider-dots{left:303px;top:572px;display:flex;gap:9px}
.slider-dots span{width:12px;height:12px;border:1.5px solid #333;border-radius:50%;background:var(--white)}
.slider-dots span.active{background:#ccc}

.section-title{font-family:"Arimo",sans-serif;font-size:25px;color:var(--ink);display:flex;align-items:center;gap:3px;white-space:nowrap}
.section-title::before{content:"";border-left:15px solid var(--ink);border-top:8px solid transparent;border-bottom:8px solid transparent;margin-right:2px}
.copy{font-size:16px;line-height:18px;color:var(--ink)}
.copy p+p{margin-top:18px}
.btn-primary{left:597px;top:542px;width:123px;height:37px;background:var(--green);color:var(--white);border-radius:4px;font-size:18px;line-height:37px;text-align:center}

.capability-list{left:143px;top:660px;width:320px;list-style:none}
.capability-list li{position:absolute;left:0;width:320px;font-size:16px}
.capability-list .label{position:absolute;left:0;width:221px;padding-left:15px;border-bottom:2px solid var(--green);height:100%}
.capability-list .label::before{content:"";position:absolute;left:0;top:50%;margin-top:-7px;width:12px;height:12px;border-radius:50%;background:var(--green-dot)}
.capability-list .more{position:absolute;left:227px;width:87px;height:20px;background:var(--grey-btn);color:var(--white);font-size:13px;line-height:20px;text-align:center;border-radius:3px}

.customers{left:0;top:915px;width:1200px;height:143px;background:var(--band)}
.customer{position:absolute;font-weight:700;color:#2a2a2a;white-space:nowrap;transform:translate(-50%,-50%)}

.site-footer{left:0;top:1058px;width:1200px;height:56px;background:var(--footer)}
.footer-nav{position:absolute;left:0;top:13px;width:1200px}
.footer-nav a,.footer-nav i{position:absolute;color:var(--white);font-size:16px;text-decoration:none;font-style:normal}
.footer-nav i{font-size:22px;top:-3px}
</style>
</head>
<body>

<header class="abs site-header">
  <div class="abs brand">RVD Worldwide Limited</div>
  <div class="abs languages">
    <svg width="34" height="34" role="img" aria-label="Chinese language"><circle cx="17" cy="17" r="16" fill="#c8201b"/></svg>
    <svg width="34" height="34" role="img" aria-label="English language"><circle cx="17" cy="17" r="16" fill="#2a3f8f"/></svg>
    <svg width="34" height="34" role="img" aria-label="Japanese language"><circle cx="17" cy="17" r="16" fill="#ffffff" stroke="#cccccc"/><circle cx="17" cy="17" r="8" fill="#d11f2b"/></svg>
  </div>
  <div class="abs phone">(02) 555- 01927</div>
  <nav class="abs main-nav">
    <a style="left:241px;top:2px">Home</a>
    <a style="left:396px;top:2px">Products</a>
    <a style="left:556px;top:2px">Services</a>
    <a style="left:712px;top:2px">About Us</a>
    <a style="left:877px;top:1px">Contact</a>
  </nav>
</header>
<div class="abs header-rule"></div>

<main class="abs content"></main>

<div class="abs facility-photo" role="img" aria-label="Photo of factory production equipment on the PCB line"></div>
<div class="abs slider-dots"><span class="active"></span><span></span><span></span><span></span></div>

<h2 class="abs section-title" style="left:598px;top:233px">Background</h2>
<div class="abs copy" style="left:598px;top:285px;width:462px">
  <p>RVD Worldwide Limited (RVD) was set up in Hong Kong in 2007 by two Hong Kong entrepreneurs, Mr. Lok Fai Tam and Mr. Wai Ho. We acquired the single sided printed circuit board factory located in Dongguan City, Guangdong Province, China, from Valtor Corporation of the U.S. in 2007. In addition to RVD, Mr. Tam and Mr. Ho also own Brightrail Systems Company Limited, a semiconductor company based in Hong Kong since 1997 with a total investment of over US$100 million. Brightrail is engaged in the manufacturing of flexible substrates and MEMS assembly business.</p>
  <p>RVD has been awarded TS 16949 and ISO14000 certificates since 2009 and 2004 respectively.</p>
</div>
<div class="abs btn-primary">Learn More</div>

<h2 class="abs section-title" style="left:116px;top:615px">Technical capability overview</h2>
<ul class="abs capability-list">
  <li style="top:4px;height:28px"><span class="label" style="padding-left:21px">Raw Materials</span><span class="more" style="top:3px">Learn More</span></li>
  <li style="top:37px;height:28px"><span class="label">Plating</span><span class="more" style="top:5px">Learn More</span></li>
  <li style="top:67px;height:27px"><span class="label">Printing Processes</span><span class="more" style="top:6px">Learn More</span></li>
  <li style="top:99px;height:28px"><span class="label">Punching And CNC Process</span><span class="more" style="top:5px">Learn More</span></li>
  <li style="top:129px;height:27px"><span class="label">V-Cut</span><span class="more" style="top:5px">Learn More</span></li>
  <li style="top:158px;height:27px"><span class="label">Surface Finishing</span><span class="more" style="top:5px">Learn More</span></li>
  <li style="top:190px;height:28px"><span class="label">Specification for carbon</span><span class="more" style="top:5px">Learn More</span></li>
</ul>

<h2 class="abs section-title" style="left:596px;top:615px">Business Principles</h2>
<div class="abs copy" style="left:596px;top:666px;width:464px">
  <p>RVD Worldwide Limited strives to be a professional top notched printed circuit board supplier. We embrace four “EXCELLENCE” principles, namely, excellence in quality, excellence in prices, excellence in services and excellence in on time delivery.</p>
  <p>We approach each customer with a long-term partnership view that delivers the lowest ownership costs and highest total values to our customers. We customize quotations and solutions in order to allow our customers to win more businesses. We believe by thinking from our customers’ points of view we will be able to create a WIN-WIN relationship.</p>
</div>

<section class="abs customers" aria-label="Customers">
  <span class="customer" style="left:235px;top:36px;font-size:21px">Halvern Industrial</span>
  <span class="customer" style="left:423px;top:38px;font-size:19px">Korvath</span>
  <span class="customer" style="left:530px;top:36px;font-size:16px">Vantrel</span>
  <span class="customer" style="left:660px;top:35px;font-size:15px">Kusanagi Drive</span>
  <span class="customer" style="left:790px;top:34px;font-size:22px">Toruni</span>
  <span class="customer" style="left:884px;top:34px;font-size:19px">Ekvo</span>
  <span class="customer" style="left:1000px;top:34px;font-size:23px">Sorada</span>
  <span class="customer" style="left:176px;top:93px;font-size:20px">Miyoden</span>
  <span class="customer" style="left:331px;top:93px;font-size:17px">Shinwa Tech</span>
  <span class="customer" style="left:492px;top:94px;font-size:23px">Palmera</span>
  <span class="customer" style="left:628px;top:93px;font-size:16px">Hisano</span>
  <span class="customer" style="left:744px;top:93px;font-size:21px">Shirota</span>
  <span class="customer" style="left:867px;top:95px;font-size:24px">Arvex</span>
  <span class="customer" style="left:997px;top:93px;font-size:24px">Dalmark</span>
</section>

<footer class="abs site-footer">
  <nav class="footer-nav">
    <a style="left:360px">Home</a><i style="left:421px">|</i>
    <a style="left:450px;font-size:15px;top:2px">Products</a><i style="left:532px">|</i>
    <a style="left:563px">Services</a><i style="left:640px">|</i>
    <a style="left:669px">About Us</a><i style="left:746px">|</i>
    <a style="left:765px">Contact</a>
  </nav>
</footer>

</body>
</html>
```